Velumin clinic business card - double sided for young clinic

I require business cards for my aesthetic clinic specialising in the below treatments. I would like the cards to be modern as my clinic base are young 22-35 years old. I require my logo on it and would like the edges to be rounded.

I have an aesthetic clinic specialising in :
Velumin
Lip Enhancement
Chemical Peels
Facial Fillers
Non Surgical Face Lift

I would the cards to have the following information on them:
My logo - (in grey/silver)
address
Phone number
services

Colours :
White/grey/silver and red

a nice image on there, perhaps a set of lips as this is a main service i deliver

Company Name: HFA Address: 52 Harwell Lane, 4 Brimfold High Street, TN7 4QW Phone: 0207 948 2176 Website: www.helenfosburyaesthetics-example.co.uk

Target Market(s)

clinics 22-45 years old mainly female

Industry/Entity Type

Business

Contact Information for Business Card

as above

Requirements
Must have
• logo
• Address
• Email
• Phone number
• Services i offer
Nice to have
• images

```html
<!DOCTYPE html>
<html lang="en">
<head>
<meta charset="utf-8">
<title>Helen Fosbury Aesthetics – Business Card</title>
<link rel="stylesheet" href="https://fonts.googleapis.com/css2?family=Cinzel:wght@400;500&family=Didact+Gothic&display=swap">
<style>
  :root {
    --backdrop: #e9eaec;
    --card-dark: #23252b;
    --card-light: #f4f4f2;
    --silver: #c9cacc;
    --ink: #26282d;
    --accent-red: #e0392f;
    --edge-red: #b3362c;
  }
  * { box-sizing: border-box; margin: 0; padding: 0; }
  html, body { width: 1200px; height: 1000px; overflow: hidden; }
  body {
    background: var(--backdrop);
    display: flex;
    align-items: center;
    justify-content: center;
    gap: 80px;
  }
  .card {
    width: 350px;
    height: 612px;
    border-radius: 14px;
    position: relative;
    box-shadow: 0 10px 30px rgba(0,0,0,.12);
    border-right: 3px solid var(--edge-red);
  }
  /* Front */
  .card--front {
    background: var(--card-dark);
    display: flex;
    flex-direction: column;
    align-items: center;
    justify-content: center;
    gap: 26px;
    padding-bottom: 40px;
  }
  .front__mark {
    width: 120px; height: 120px;
    border-radius: 50%;
    background: var(--silver);
  }
  .front__name {
    font-family: "Cinzel", serif;
    font-weight: 400;
    color: var(--silver);
    text-align: center;
    font-size: 25px;
    letter-spacing: 3px;
    line-height: 1.3;
  }
  /* Back */
  .card--back {
    background: var(--card-light);
    font-family: "Didact Gothic", sans-serif;
    color: var(--ink);
    text-align: center;
    padding: 64px 24px 0;
  }
  .back__brand {
    display: flex;
    align-items: center;
    justify-content: center;
    gap: 10px;
  }
  .back__dot {
    width: 18px; height: 18px;
    border-radius: 50%;
    background: var(--card-dark);
  }
  .back__initials {
    font-family: "Didact Gothic", sans-serif;
    font-size: 30px;
    letter-spacing: 4px;
    color: var(--ink);
  }
  .back__tagline {
    margin-top: 22px;
    color: var(--accent-red);
    font-size: 15px;
    letter-spacing: 2.5px;
    line-height: 1.3;
  }
  .contact { margin-top: 58px; display: flex; flex-direction: column; align-items: center; }
  .contact__icon { width: 18px; height: 18px; margin-bottom: 10px; }
  .contact__text {
    font-size: 15px;
    letter-spacing: 2px;
    line-height: 1.4;
    margin-bottom: 16px;
  }
  .contact__text--email { font-size: 13px; letter-spacing: 1px; }
  .back__web {
    position: absolute;
    left: 0; right: 0; bottom: 44px;
    display: flex; flex-direction: column; align-items: center;
  }
  .back__web-text { font-size: 12.5px; letter-spacing: 1.2px; margin-top: 10px; }
</style>
</head>
<body>
  <section class="card card--front">
    <div class="front__mark"></div>
    <h1 class="front__name">Helen Fosbury<br>Aesthetics</h1>
  </section>

  <section class="card card--back">
    <div class="back__brand">
      <span class="back__dot"></span>
      <span class="back__initials">HFA</span>
    </div>
    <p class="back__tagline">ACHIEVE A FRESH AND<br>BEAUTIFUL YOU</p>

    <div class="contact">
      <svg class="contact__icon" viewBox="0 0 24 24" fill="none" stroke="currentColor" stroke-width="1.6">
        <rect x="7" y="3" width="10" height="18" rx="2"/><line x1="11" y1="18" x2="13" y2="18"/>
      </svg>
      <p class="contact__text">020 7948 2176</p>

      <svg class="contact__icon" viewBox="0 0 24 24" fill="currentColor">
        <path d="M3 6h18v12H3z"/><path d="M3 6l9 7 9-7" fill="none" stroke="#f4f4f2" stroke-width="1.4"/>
      </svg>
      <p class="contact__text contact__text--email">hfabrimfoldbookings@example.com</p>

      <svg class="contact__icon" viewBox="0 0 24 24" fill="currentColor">
        <path d="M12 2a7 7 0 0 0-7 7c0 5 7 13 7 13s7-8 7-13a7 7 0 0 0-7-7zm0 10a3 3 0 1 1 0-6 3 3 0 0 1 0 6z"/>
      </svg>
      <p class="contact__text">4 Brimfold Parade,<br>Sussex, TN7 4QW</p>
    </div>

    <div class="back__web">
      <svg class="contact__icon" viewBox="0 0 24 24" fill="currentColor">
        <path d="M7 3l11 11h-6l3.5 7-2.3 1-3.4-7L7 19z"/>
      </svg>
      <p class="back__web-text">helenfosburyaesthetics-example.co.uk</p>
    </div>
  </section>
</body>
</html>
```